AI Business Tools Landing Page

My web-based website builder (Brindora.com) will be adding many new features in the very near future and I need an eye-catching landing page to promote these new products.

The page will have a primary section of the 8 main products we are promoting:
1. AI Instant Website Generator
2. AI Chatbot
3. Online Store Builder with AI Assistance
4. AI Auto-Blogging System
5. Online Scheduling System
6. Custom Email System
7. SEO Service
8. CRM System

The page will also have a smaller section for links to our affiliate programs. These can be smaller, less-promanent buttons or links. These are the affiliate products:
1. Get Your LLC
2. Website Design and Maintenance
3. Vorlo Ads Management
4. Social Media Posting Service
5. Logo Design
6. Trademark Registration
7. Patent Application
8. Printing Services (including postcards, flyers, and merch.)
9. Bulk AI Content Generator

The theme and color scheme of the page should follow the theme of our main website, which is https://brindora.com.

I need the page fully coded and ready to deploy on my server.

I look forward to seeing your amazing designs!

```html
<!DOCTYPE html>
<html lang="en">
<head>
<meta charset="utf-8">
<title>AI Business Tools – Brindora</title>
<link rel="stylesheet" href="https://fonts.googleapis.com/css2?family=Audiowide&family=Poppins:wght@400;500;600&display=swap">
<style>
  :root{
    --navy:#04213f;
    --navy-deep:#021a33;
    --card:#101010;
    --icon-tile:#06213d;
    --accent:#2ec4e8;
    --sky-top:#35c9e8;
    --sky-mid:#1a98e6;
    --sky-low:#0a6ee0;
    --white:#ffffff;
    --edge:#cfeff8;
    --btn-a:#1aa8ef;
    --btn-b:#0a6fe0;
  }
  *{box-sizing:border-box;margin:0;padding:0}
  html,body{width:1200px;height:2400px;overflow:hidden}
  body{
    position:relative;
    font-family:"Poppins",sans-serif;
    color:var(--white);
    background:linear-gradient(180deg,var(--sky-top) 640px,var(--sky-mid) 1300px,var(--sky-low) 2000px,#0b63d8 2240px);
  }
  .site-header{
    position:absolute;left:0;top:0;width:1200px;height:79px;background:var(--navy);
  }
  .brand{
    position:absolute;left:95px;top:20px;display:flex;align-items:center;gap:10px;
    font-family:"Poppins",sans-serif;font-weight:500;font-size:27px;color:var(--white);
  }
  .brand-dot{width:36px;height:36px;border-radius:50%;background:var(--accent)}
  .contact-btn{
    position:absolute;left:988px;top:22px;width:117px;height:35px;border-radius:18px;
    background:linear-gradient(180deg,var(--btn-a),var(--btn-b));
    font-weight:600;font-size:12px;letter-spacing:.2px;color:var(--white);
    display:flex;align-items:center;justify-content:center;text-decoration:none;
    box-shadow:0 4px 14px rgba(0,0,0,.45);
  }
  .hero{
    position:absolute;left:0;top:79px;width:1200px;height:556px;
    border-radius:0 0 110px 110px;overflow:hidden;
    background:
      radial-gradient(circle at 82% 35%,rgba(210,240,255,.55) 0 10%,transparent 26%),
      radial-gradient(circle at 45% 90%,rgba(40,220,140,.45) 0 6%,transparent 22%),
      radial-gradient(circle at 55% 20%,rgba(40,200,160,.35) 0 8%,transparent 30%),
      linear-gradient(160deg,#082a63 0%,#0b3a9a 45%,#0a5fd0 75%,#0b4fbf 100%);
  }
  .hero-panel{
    position:absolute;left:157px;top:150px;width:886px;height:258px;
    border:3px solid var(--white);border-radius:40px;
    background:rgba(2,18,50,.55);
    text-align:center;padding:48px 70px 0;
  }
  .hero-title{
    font-family:"Audiowide",sans-serif;font-weight:400;font-size:34px;letter-spacing:1px;
  }
  .hero-copy{margin-top:20px;font-size:13.6px;line-height:20.5px}

  .product{
    position:absolute;width:464px;background:var(--card);
    border:2px solid var(--edge);border-radius:20px;overflow:hidden;
  }
  .icon-tile{
    position:absolute;left:0;top:0;width:98px;height:98px;background:var(--icon-tile);
    border-radius:0 0 20px 0;display:flex;align-items:center;justify-content:center;
  }
  .product h2{
    margin:30px 24px 0 122px;font-family:"Audiowide",sans-serif;font-weight:400;
    font-size:14.6px;line-height:20px;color:var(--accent);
  }
  .product ul{list-style:none;margin:12px 16px 0 122px}
  .product li{position:relative;padding-left:20px;font-size:12.4px;line-height:20.5px}
  .product li svg{position:absolute;left:0;top:4px}

  .extras-title{
    position:absolute;left:0;top:1738px;width:1200px;text-align:center;
    font-family:"Audiowide",sans-serif;font-size:24.5px;font-weight:400;
  }
  .extra{
    position:absolute;width:303px;height:120px;background:var(--navy);
    border:2px solid var(--edge);border-radius:20px;overflow:hidden;
  }
  .extra .icon-tile{width:72px;height:72px;background:#0c1118;border-radius:0 0 18px 0}
  .extra h3{
    position:absolute;left:94px;top:34px;right:14px;
    font-family:"Audiowide",sans-serif;font-weight:400;font-size:14px;line-height:18px;
  }
  .site-footer{
    position:absolute;left:0;top:2240px;width:1200px;height:160px;background:var(--navy);
    text-align:center;
  }
  .social{display:flex;justify-content:center;gap:11px;margin-top:50px}
  .social span{width:14px;height:14px;border-radius:50%;background:var(--white)}
  .copyright{margin-top:34px;font-size:9px;font-weight:500;letter-spacing:.3px}
</style>
</head>
<body>

<header class="site-header">
  <div class="brand"><span class="brand-dot"></span>Brindora</div>
  <a class="contact-btn" href="https://brindora.com">CONTACT US</a>
</header>

<section class="hero" role="img" aria-label="Illustration of a friendly white robot beside glowing data screens on a blue circuit board">
  <div class="hero-panel">
    <h1 class="hero-title">AI BUSINESS TOOLS</h1>
    <p class="hero-copy">Our goal extends far beyond just website creation. We are dedicated to nurturing a community that champions innovation and breaks down entry barriers. By constantly enhancing our algorithms, staying ahead of contemporary design trends, and, crucially, valuing the feedback from you, our users, we ensure that Brindora.com stays at the cutting edge of digital innovation.</p>
  </div>
</section>

<svg width="0" height="0" style="position:absolute">
  <defs>
    <symbol id="tick" viewBox="0 0 12 12"><circle cx="6" cy="6" r="5.2" fill="none" stroke="#2ec4e8" stroke-width="1"/><path d="M3.6 6.2l1.7 1.7 3.2-3.4" fill="none" stroke="#2ec4e8" stroke-width="1"/></symbol>
  </defs>
</svg>

<!-- Row 1 -->
<article class="product" style="left:126px;top:682px;height:205px">
  <div class="icon-tile"><svg width="54" height="54" viewBox="0 0 54 54" fill="none" stroke="#2ec4e8" stroke-width="1.6"><rect x="6" y="10" width="42" height="28" rx="2"/><path d="M2 42h50l-3 4H5z"/><circle cx="27" cy="20" r="6"/><path d="M27 26v8M20 30h14"/></svg></div>
  <h2>AI Instant Website Generator</h2>
  <ul>
    <li><svg width="12" height="12"><use href="#tick"/></svg>Get a professional, SEO-optimized website in seconds!</li>
    <li><svg width="12" height="12"><use href="#tick"/></svg>Includes custom domain, secure high-speed hosting, professional images, and more!</li>
  </ul>
</article>
<article class="product" style="left:609px;top:682px;height:205px">
  <div class="icon-tile"><svg width="54" height="54" viewBox="0 0 54 54" fill="none" stroke="#2ec4e8" stroke-width="1.6"><rect x="10" y="14" width="34" height="26" rx="10"/><circle cx="21" cy="26" r="3"/><circle cx="33" cy="26" r="3"/><path d="M27 14V8M22 40l-2 6 7-6"/><path d="M6 22v10M48 22v10"/></svg></div>
  <h2>AI ChatBot</h2>
  <ul>
    <li><svg width="12" height="12"><use href="#tick"/></svg>Fully-trainable ChatBot will learn about your business to automate the customer support process!</li>
    <li><svg width="12" height="12"><use href="#tick"/></svg>Built-in CRM features integrate emailing, text messaging, and contact forms!</li>
  </ul>
</article>

<!-- Row 2 -->
<article class="product" style="left:126px;top:906px;height:224px">
  <div class="icon-tile"><svg width="54" height="54" viewBox="0 0 54 54" fill="none" stroke="#2ec4e8" stroke-width="1.6"><path d="M10 8h34l4 10H6z"/><rect x="14" y="18" width="26" height="30" rx="2"/><path d="M19 28h16l-2 8H21z"/><circle cx="22" cy="41" r="1.5"/><circle cx="32" cy="41" r="1.5"/></svg></div>
  <h2>Online Store Builder (E-Commerce) with AI Assistance</h2>
  <ul>
    <li><svg width="12" height="12"><use href="#tick"/></svg>Sell you products online and integrate your products into any website!</li>
    <li><svg width="12" height="12"><use href="#tick"/></svg>Accept payments from multiple payment gateways including Paxly and Coinrail!</li>
  </ul>
</article>
<article class="product" style="left:609px;top:906px;height:224px">
  <div class="icon-tile"><svg width="54" height="54" viewBox="0 0 54 54" fill="none" stroke="#2ec4e8" stroke-width="1.6"><rect x="4" y="6" width="46" height="36" rx="2"/><path d="M4 13h46M12 20h30M12 26h14M12 32h14M22 42l4 6 4-6"/><rect x="30" y="25" width="12" height="10"/></svg></div>
  <h2>AI Auto-Blogging System</h2>
  <ul>
    <li><svg width="12" height="12"><use href="#tick"/></svg>AI will generate an incredible blog for your business in seconds and immediately begin posting content for you!</li>
    <li><svg width="12" height="12"><use href="#tick"/></svg>Choose from daily, weekly, or monthly automated blog posting. Consistent, unique, SEO-optimized content posting on cruise control!</li>
  </ul>
</article>

<!-- Row 3 -->
<article class="product" style="left:126px;top:1150px;height:223px">
  <div class="icon-tile"><svg width="54" height="54" viewBox="0 0 54 54" fill="none" stroke="#2ec4e8" stroke-width="1.6"><rect x="4" y="8" width="40" height="34" rx="2"/><path d="M4 15h40M12 4v7M36 4v7"/><rect x="10" y="20" width="6" height="6"/><rect x="20" y="20" width="6" height="6"/><rect x="10" y="30" width="6" height="6"/><circle cx="40" cy="34" r="10" fill="#06213d"/><path d="M40 28v6l4 3"/><path d="M2 46h30"/></svg></div>
  <h2>Online Scheduling System</h2>
  <ul>
    <li><svg width="12" height="12"><use href="#tick"/></svg>Get appointment bookings, restaurant reservations, or consultations scheduled directly from your website!</li>
    <li><svg width="12" height="12"><use href="#tick"/></svg>Manage your employees' schedules and all your appointments from a simple, user-friendly dashboard!</li>
  </ul>
</article>
<article class="product" style="left:609px;top:1150px;height:223px">
  <div class="icon-tile"><svg width="54" height="54" viewBox="0 0 54 54" fill="none" stroke="#2ec4e8" stroke-width="1.6"><path d="M4 22l23-16 23 16v26H4z"/><path d="M4 22l23 16 23-16M4 48l17-14M50 48L33 34"/><circle cx="27" cy="20" r="4"/></svg></div>
  <h2>Custom Emails Using Your Domain</h2>
  <ul>
    <li><svg width="12" height="12"><use href="#tick"/></svg>Quickly set up emails for yourself and all your employees with your own domain extension (example – johnd@yoursite.com). No more unprofessional Mailvio and Yandor email addresses!</li>
    <li><svg width="12" height="12"><use href="#tick"/></svg>Manage all your business emails from a simple, user-friendly interface!</li>
  </ul>
</article>

<!-- Row 4 -->
<article class="product" style="left:126px;top:1393px;height:265px">
  <div class="icon-tile"><svg width="54" height="54" viewBox="0 0 54 54" fill="none" stroke="#2ec4e8" stroke-width="1.6"><rect x="4" y="6" width="38" height="30" rx="2"/><rect x="10" y="14" width="40" height="32" rx="2" fill="#06213d"/><path d="M10 21h40"/><rect x="18" y="28" width="12" height="8" rx="4"/><rect x="28" y="28" width="12" height="8" rx="4"/></svg></div>
  <h2>SEO Service – Automatic Backlink Building</h2>
  <ul>
    <li><svg width="12" height="12"><use href="#tick"/></svg>Let us do the hard work of getting high-quality backlinks to your website. Although difficult to get, backlinks to your website boost search engine ranking more than any other strategy!</li>
    <li><svg width="12" height="12"><use href="#tick"/></svg>Subscribe now and start getting 10-20 high-quality permanent backlinks to your website every month, guaranteed!</li>
  </ul>
</article>
<article class="product" style="left:609px;top:1393px;height:265px">
  <div class="icon-tile"><svg width="54" height="54" viewBox="0 0 54 54" fill="none" stroke="#2ec4e8" stroke-width="1.6"><circle cx="27" cy="18" r="8"/><circle cx="27" cy="18" r="3"/><path d="M27 26v10M27 36L10 40M27 36l17 4M27 36v8"/><circle cx="8" cy="42" r="3"/><circle cx="46" cy="42" r="3"/><circle cx="27" cy="47" r="3"/><circle cx="8" cy="22" r="3"/><circle cx="46" cy="22" r="3"/></svg></div>
  <h2>Customer Relationship Management (CRM) System</h2>
  <ul>
    <li><svg width="12" height="12"><use href="#tick"/></svg>Automate the lead follow up process to consistently stay in front of your potential customers!</li>
    <li><svg width="12" height="12"><use href="#tick"/></svg>Schedule automatic email and text campaigns and effortlessly follow your funnels from lead to closing!</li>
  </ul>
</article>

<h2 class="extras-title">Additional Resources to Help Launch Your Business</h2>

<!-- Extras -->
<a class="extra" style="left:126px;top:1791px"><div class="icon-tile"><svg width="38" height="38" viewBox="0 0 38 38" fill="none" stroke="#9aa3ad" stroke-width="1.3"><rect x="12" y="8" width="12" height="28"/><rect x="4" y="20" width="8" height="16"/><rect x="24" y="22" width="8" height="14"/><path d="M18 2v6M15 14h6M15 20h6M15 26h6"/></svg></div><h3>Get Your LLC</h3></a>
<a class="extra" style="left:449px;top:1791px"><div class="icon-tile"><svg width="38" height="38" viewBox="0 0 38 38" fill="none" stroke="#9aa3ad" stroke-width="1.3"><rect x="4" y="4" width="30" height="22" rx="1"/><path d="M10 10h6M10 15h6M10 20h6M22 10v12M27 10v12M4 32h30M19 26v6"/></svg></div><h3>Website Design and Maintenance</h3></a>
<a class="extra" style="left:771px;top:1791px"><div class="icon-tile"><svg width="38" height="38" viewBox="0 0 38 38" fill="none" stroke="#9aa3ad" stroke-width="1.3"><rect x="3" y="5" width="32" height="22" rx="1"/><path d="M8 12l8-4v14l-8-4zM21 12h9M21 17h9M21 22h6M13 32h12M19 27v5"/></svg></div><h3>Vorlo Ads Management</h3></a>

<a class="extra" style="left:126px;top:1930px"><div class="icon-tile"><svg width="38" height="38" viewBox="0 0 38 38" fill="none" stroke="#9aa3ad" stroke-width="1.3"><rect x="4" y="4" width="30" height="30" rx="7"/><circle cx="19" cy="19" r="7"/><circle cx="19" cy="19" r="3.5"/></svg></div><h3>Social Media Posting Service</h3></a>
<a class="extra" style="left:449px;top:1930px"><div class="icon-tile"><svg width="38" height="38" viewBox="0 0 38 38" fill="none" stroke="#9aa3ad" stroke-width="1.3"><path d="M19 6L8 34M19 6l11 28M12 24h14M4 6h30"/><circle cx="19" cy="6" r="2"/></svg></div><h3>Logo Design</h3></a>
<a class="extra" style="left:771px;top:1930px"><div class="icon-tile"><svg width="38" height="38" viewBox="0 0 38 38" fill="none" stroke="#9aa3ad" stroke-width="1.3"><circle cx="19" cy="19" r="15"/><text x="19" y="24" text-anchor="middle" font-family="Poppins,sans-serif" font-size="13" fill="#9aa3ad" stroke="none">TM</text></svg></div><h3>Trademark Registration</h3></a>

<a class="extra" style="left:126px;top:2069px"><div class="icon-tile"><svg width="38" height="38" viewBox="0 0 38 38" fill="none" stroke="#9aa3ad" stroke-width="1.3"><path d="M8 4h16l6 6v22H8z"/><path d="M13 12h12M13 17h12M13 22h8"/><circle cx="14" cy="30" r="4"/></svg></div><h3>Patent Application</h3></a>
<a class="extra" style="left:449px;top:2069px"><div class="icon-tile"><svg width="38" height="38" viewBox="0 0 38 38" fill="none" stroke="#9aa3ad" stroke-width="1.3"><rect x="8" y="4" width="22" height="30" rx="1"/><circle cx="19" cy="13" r="3"/><path d="M12 24l5-5 4 3 5-4M12 29h14"/></svg></div><h3>Printing Services (including postcards, flyers, and merch.)</h3></a>
<a class="extra" style="left:771px;top:2069px"><div class="icon-tile"><svg width="38" height="38" viewBox="0 0 38 38" fill="none" stroke="#9aa3ad" stroke-width="1.3"><rect x="8" y="12" width="22" height="16" rx="4"/><path d="M19 12V6M4 18v6M34 18v6M16 20l4 2-4 2z"/><circle cx="19" cy="5" r="1.5"/></svg></div><h3>Bulk AI Content Generator</h3></a>

<footer class="site-footer">
  <div class="social"><span></span><span></span><span></span><span></span></div>
  <p class="copyright">COPYRIGHT © 2024 BRINDORA. ALL RIGHTS RESERVED.</p>
</footer>

</body>
</html>
```